TIVARELCAP web-presence redisign

We would like to have our existing web-presence redesigned. Have a look at www.tivarel.ch (please use explorer). To the existing 11 pages we would add one more.

```html
<!DOCTYPE html>
<html lang="de">
<head>
<meta charset="utf-8">
<title>Tivarel Zahnarztpraxis</title>
<link rel="stylesheet" href="https://fonts.googleapis.com/css2?family=Open+Sans:ital,wght@0,300;0,400;0,600;1,400&display=swap">
<style>
:root{
  --accent:#c6743a;
  --accent-soft:#d08a55;
  --ink:#1f1f1f;
  --muted:#6f6f6f;
  --label:#7f7f7f;
  --line:#cfcfcf;
  --paper:#ffffff;
}
*{box-sizing:border-box;margin:0;padding:0}
html,body{width:1200px;height:1149px;overflow:hidden;background:var(--paper)}
body{position:relative;font-family:"Open Sans",Arial,sans-serif;color:var(--ink)}
.abs{position:absolute}

.phone-tab{left:834px;top:0;width:180px;height:32px;background:var(--accent);color:#fff;
  font-style:italic;font-size:14px;display:flex;align-items:center;justify-content:center;gap:8px}

.brand{left:187px;top:34px;display:flex;align-items:center;gap:12px}
.brand-dot{width:52px;height:52px;border-radius:50%;background:#d9a441}
.brand-name{font-size:20px;line-height:24px;color:#6b5a3a;font-weight:400}

.main-nav{left:514px;top:72px;display:flex;gap:15px;font-size:15px}
.main-nav a{color:var(--ink);text-decoration:none;padding-bottom:3px}
.main-nav a.active{border-bottom:3px solid #8a8a8a}

.hero{left:187px;top:124px;width:826px;height:433px;
  background:linear-gradient(90deg,#f4f4f2 0%,#ece9e6 40%,#c9a48d 62%,#b58a6f 80%,#d8c3b3 100%)}
.hero-text{left:227px;top:261px;font-size:21px;font-weight:300;line-height:26px;color:#222}
.hero-mark{left:358px;top:330px;width:10px;height:10px;border-radius:50%;background:var(--accent)}
.hero-btn{left:229px;top:344px;width:270px;height:75px;border:1px solid var(--accent);
  color:var(--accent);font-size:18px;line-height:22px;text-align:center;display:flex;align-items:center;justify-content:center}
.slide-arrow{top:326px;width:33px;height:33px}

.welcome-mark{left:188px;top:626px;width:18px;height:18px;border-radius:50%;background:var(--accent)}
.welcome-title{left:213px;top:620px;font-size:24px;color:var(--accent);font-weight:400}
.dotted{left:187px;top:661px;width:544px;border-top:3px dotted var(--line)}
.lead{left:187px;top:675px;width:560px;font-size:16px;line-height:22.5px;color:#333}
.lead strong{font-weight:600;color:var(--ink)}
.body-copy{left:187px;top:752px;width:560px;font-size:11.4px;line-height:18px;color:#222}

.services{left:187px;top:829px;width:547px;height:181px;background:#fff;
  box-shadow:0 0 3px rgba(0,0,0,.25)}
.service{position:absolute;top:17px;width:166px}
.service-photo{height:116px}
.service-label{margin-top:4px;height:27px;background:var(--label);color:#fff;
  font-size:15px;text-align:center;line-height:27px}

.aside{left:768px;top:618px;width:245px;height:392px;background:#fff;
  box-shadow:0 0 3px rgba(0,0,0,.25)}
.aside-title{position:absolute;left:0;top:16px;width:100%;text-align:center;font-size:16px}
.aside-photo{position:absolute;left:10px;top:51px;width:225px;height:95px;
  background:linear-gradient(90deg,#5a3a2c,#a07060 25%,#3a2a22 50%,#a57a66 75%,#4a3328)}
.aside-caption{position:absolute;left:0;top:160px;width:100%;text-align:center;font-size:11px;line-height:13px}
.map{position:absolute;left:0;top:220px;width:245px;height:118px;background:#e6e2da}
.map-label{position:absolute;left:134px;top:90px;font-size:8px;font-weight:600;color:#8b1d1d}
.contact-band{position:absolute;left:0;top:338px;width:245px;height:54px;background:var(--accent-soft);
  color:#fff;font-size:11px;line-height:14px;text-align:center;padding-top:13px}

.footer-rule{left:187px;top:1045px;width:826px;border-top:1px dashed #c4c4c4}
.footer-mark{left:591px;top:1037px;width:16px;height:16px;border-radius:50%;background:#fff;border:1px solid #d2d2d2}
.footer-nav{left:186px;top:1066px;display:flex;gap:12px;font-size:11.5px;color:var(--muted)}
.copyright{left:187px;top:1087px;font-size:11.5px;color:var(--muted)}
.social{left:920px;top:1074px;display:flex;gap:10px;font-size:11px;color:#8a8a8a}
</style>
</head>
<body>

<div class="abs phone-tab">
  <svg width="12" height="14" viewBox="0 0 12 14"><path d="M3 1 L5 4 L3.5 5.5 Q5 9 7.5 10.5 L9 9 L11.5 11.5 L10 13 Q4 12 1 3 Z" fill="#fff"/></svg>
  <span>+41 (0)44 555 01 23</span>
</div>

<div class="abs brand">
  <span class="brand-dot"></span>
  <span class="brand-name">Tivarel<br>Zahnarztpraxis</span>
</div>

<nav class="abs main-nav">
  <a href="#">Home</a>
  <a href="#" class="active">Zahnmedizin</a>
  <a href="#">Dentalhygiene</a>
  <a href="#">Before &amp; After</a>
  <a href="#">Team</a>
  <a href="#">Kontakt</a>
</nav>

<div class="abs hero" role="img" aria-label="Two smiling young women posing together on a bright background"></div>
<p class="abs hero-text">Lorem ipsum dolor sit amet sid<br>consectetur adipiscing elit.</p>
<span class="abs hero-mark"></span>
<a class="abs hero-btn" href="#">REQUEST<br>A FREE CONSULTATION</a>
<svg class="abs slide-arrow" style="left:138px" viewBox="0 0 33 33"><circle cx="16.5" cy="16.5" r="15.5" fill="none" stroke="#bbb" stroke-width="1.5"/><path d="M19 10 L13 16.5 L19 23" fill="none" stroke="#bbb" stroke-width="1.5"/></svg>
<svg class="abs slide-arrow" style="left:1031px" viewBox="0 0 33 33"><circle cx="16.5" cy="16.5" r="15.5" fill="none" stroke="#bbb" stroke-width="1.5"/><path d="M14 10 L20 16.5 L14 23" fill="none" stroke="#bbb" stroke-width="1.5"/></svg>

<span class="abs welcome-mark"></span>
<h1 class="abs welcome-title">Welcome to Tivarel Zahnarztpraxis</h1>
<div class="abs dotted"></div>
<p class="abs lead"><strong>Dr. med. Lena Brunner-Keller,</strong> It is our goal to improve your wellbeing. You will enjoy the beauty of everyday life with healthy teeth and laugh heartily in every situation.</p>
<p class="abs body-copy">Lorem ipsum dolor sit amet, consectetur adipiscing elit. In fermentum dolor non augue pretium egestas. Donec sem eros, tincidunt at congue ut, posuere sit amet est. Vivamus scelerisque viverra odio sit amet laoreet. Ut nec neque non justo rutrum tempor lobortis eu ante.</p>

<section class="abs services">
  <div class="service" style="left:19px">
    <div class="service-photo" role="img" aria-label="Smiling woman holding a red apple in a green field" style="background:linear-gradient(135deg,#7fa24a,#c9a08a 55%,#8e3f8e)"></div>
    <div class="service-label">Gesundheit</div>
  </div>
  <div class="service" style="left:193px">
    <div class="service-photo" role="img" aria-label="Dental technician shaping a denture model" style="background:linear-gradient(135deg,#e6e8ea,#c9c4bd 50%,#d9b59a)"></div>
    <div class="service-label">Ästhetik</div>
  </div>
  <div class="service" style="left:366px">
    <div class="service-photo" role="img" aria-label="Dentist treating a patient in the chair" style="background:linear-gradient(135deg,#e9d2c0,#cfd9dd 55%,#8fc3d4)"></div>
    <div class="service-label">Lösungen</div>
  </div>
</section>

<aside class="abs aside">
  <h2 class="aside-title" style="font-weight:400">Before and After</h2>
  <div class="aside-photo" role="img" aria-label="Before and after photos of a patient's smile"></div>
  <p class="aside-caption">Click here and See the<br>results we have created for yourself</p>
  <div class="map" role="img" aria-label="Street map showing the practice location">
    <svg style="position:absolute;left:122px;top:62px" width="16" height="26" viewBox="0 0 16 26"><path d="M8 1 C3 1 1 5 1 8 C1 13 8 20 8 25 C8 20 15 13 15 8 C15 5 13 1 8 1 Z" fill="#d9322b"/><circle cx="8" cy="8" r="3" fill="#8b1d1d"/></svg>
    <span class="map-label">TIVARELCAP</span>
  </div>
  <div class="contact-band">Add: Lindenweg 12 CH-8600 Seedorf<br>Email : info@tivarel.ch</div>
</aside>

<div class="abs footer-rule"></div>
<span class="abs footer-mark"></span>
<nav class="abs footer-nav">
  <span>Home</span><span>Zahnmedizin</span><span>Dentalhygiene</span><span>Before &amp; After</span><span>Team</span><span>Kontakt</span>
</nav>
<p class="abs copyright">All rights reserved © 2014 - Privacy Policy</p>
<div class="abs social"><span>Circlepage</span><span>Chirpline</span></div>

</body>
</html>
```